Facebook and Instagram advertisment

We need Facebook and Instagram ads.  Simple ad with Alaska themed background.
This ad is to introduce our new KORVO Internet service.
--Speeds to 500 mbps
-- Packages start at only $89.99 for speeds to 100mbps
-- Fiber Optic based connection, Not satellite
-- Extreme low latency, consistent speeds
--FREE equipment, FREE Installation, FREE wifi router, First month of service FREE

Logo Text
This is for a Facebook/Instagram ad. We already have a logo

```html
<!DOCTYPE html>
<html lang="en">
<head>
<meta charset="utf-8">
<title>KORVO Internet – Social Ad</title>
<link rel="stylesheet" href="https://fonts.googleapis.com/css2?family=Barlow:wght@400;600;700&family=Barlow+Condensed:wght@700&display=swap">
<style>
  :root {
    --night-deep: #0a1838;
    --night-mid: #14306a;
    --aurora-violet: #6a3fb0;
    --aurora-teal: #1fb7b0;
    --aurora-blue: #2f5fb0;
    --text-white: #ffffff;
  }
  html, body {
    margin: 0;
    padding: 0;
    overflow: hidden;
    background: var(--night-deep);
  }
  .ad {
    position: relative;
    width: 1200px;
    height: 1200px;
    overflow: hidden;
    color: var(--text-white);
    font-family: "Barlow", Arial, sans-serif;
  }
  .ad__sky {
    position: absolute;
    inset: 0;
    background:
      radial-gradient(ellipse 420px 260px at 560px 40px, rgba(140, 70, 200, 0.75), transparent 70%),
      radial-gradient(ellipse 700px 180px at 720px 330px, rgba(31, 183, 176, 0.55), transparent 70%),
      radial-gradient(ellipse 520px 220px at 1050px 200px, rgba(31, 183, 176, 0.45), transparent 70%),
      radial-gradient(ellipse 500px 360px at 330px 560px, rgba(47, 95, 176, 0.6), transparent 70%),
      radial-gradient(ellipse 360px 200px at 520px 760px, rgba(31, 160, 170, 0.35), transparent 70%),
      linear-gradient(180deg, #2b2a78 0%, var(--night-mid) 35%, #11285c 60%, var(--night-deep) 100%);
  }
  .brand {
    position: absolute;
    top: 132px;
    left: 668px;
    display: flex;
    align-items: center;
    gap: 16px;
  }
  .brand__dot {
    width: 22px;
    height: 22px;
    border-radius: 50%;
    background: var(--text-white);
  }
  .brand__name {
    font-family: "Barlow", Arial, sans-serif;
    font-weight: 600;
    font-size: 58px;
    line-height: 1;
    color: var(--text-white);
  }
  .offer {
    position: absolute;
    left: 62px;
    top: 440px;
    width: 1100px;
  }
  .offer__product {
    margin: 0;
    font-family: "Barlow Condensed", "Arial Narrow", sans-serif;
    font-weight: 700;
    font-size: 292px;
    line-height: 0.9;
    letter-spacing: 2px;
  }
  .offer__headline {
    margin: 28px 0 0;
    font-weight: 600;
    font-size: 58px;
    line-height: 1.05;
  }
  .offer__line {
    margin: 0;
    font-size: 33px;
    line-height: 1.2;
    font-weight: 400;
  }
  .offer__line--first { margin-top: 6px; }
  .offer__line--spaced { margin-top: 20px; }
  .offer__line strong { font-weight: 700; }
  .perks {
    margin-top: 82px;
  }
  .perks .offer__line {
    font-size: 38px;
    line-height: 1.4;
  }
</style>
</head>
<body>
  <main class="ad">
    <div class="ad__sky" role="img" aria-label="Alaskan night sky with violet and teal northern lights, scattered stars and a shooting star"></div>

    <div class="brand">
      <span class="brand__dot"></span>
      <span class="brand__name">Tundra Link</span>
    </div>

    <section class="offer">
      <h1 class="offer__product">KORVO</h1>
      <p class="offer__headline">Speeds to 500 mbps</p>
      <p class="offer__line offer__line--first">Packages start at only $89.99 for speeds to 100mbps</p>
      <p class="offer__line offer__line--spaced"><strong>FIBER OPTIC</strong> based connection, Not satellite</p>
      <p class="offer__line offer__line--spaced"><strong>EXTREME LOW LATENCY,</strong> consistent speeds</p>

      <div class="perks">
        <p class="offer__line"><strong>FREE</strong> equipment, <strong>FREE</strong> Installation,</p>
        <p class="offer__line"><strong>FREE</strong> wifi router, <strong>First month of service FREE</strong></p>
      </div>
    </section>
  </main>
</body>
</html>
```